Baby Care Print Log for Nannies and Parents- Creating a brand/style I can use across different forms

I am creating a notebook for babysitters to use to communicate with parents about the children they care for. I will be creating many different forms (emergency contacts, daily logs, shopping lists, etc.)
I need a look and feel from which to style these forms from. I am starting by designing the daily baby care log. I need a designer to take my Word doc with just text on it, and create a visual approach to make this visually appealing.
I do not want this to be extremely "babyish" with cartoon styling. I want it to be more of a professional looking style. I would like to be able to color each different document a different color palette, yet keep the similar look and feel. My logo is attached for inspiration. I use real photography across my website velmorapath.com.
Updates
I will be re-designing my Wordpress website based on what design I like best and also will need other forms completed once I pick a design. I am hoping to work with someone who I can hire for further development needs as well. Added Saturday, February 11, 2017
Target Market(s)
Professional Parents
Industry/Entity Type
Education
Requirements
Must have
- color, pop, visual appeal
- Please use the color in my logo and any complementary colors that you think work well with it. I definitely like colored patterns, ombre, colored backgrounds, etc. I'd prefer for it not to be completely white with only pops of color here and there.
Nice to have
- My logo somewhere subtly on the form
- Photography elements
Should not have
- cartoon images of babies, etc. I use real photography across my website with the exception of my logo umbrella.

```html
<!DOCTYPE html>
<html lang="en">
<head>
<meta charset="utf-8">
<title>Velmora Notes – Daily Baby Care Log</title>
<link rel="stylesheet" href="https://fonts.googleapis.com/css2?family=Questrial&display=swap">
<style>
  :root{
    --page-bg:#d9d9dc;
    --ink:#2a2a2a;
    --cyan:#12b8d8;
    --green:#8dc63f;
    --orange:#f37021;
    --pink:#e2449a;
    --card:#ffffff;
  }
  *{box-sizing:border-box;margin:0;padding:0}
  html,body{width:1200px;height:1200px;overflow:hidden;background:var(--page-bg)}
  body{font-family:"Questrial",sans-serif;color:var(--ink)}
  .sheet{
    position:absolute;left:192px;top:24px;width:992px;height:1402px;
    transform:scale(0.8217);transform-origin:top left;overflow:hidden;
  }
  .sheet-photo{
    position:absolute;inset:0;
    background:
      radial-gradient(ellipse 420px 340px at 820px 190px,#f6dccd 0%,rgba(246,220,205,0) 70%),
      radial-gradient(ellipse 500px 260px at 200px 90px,#f4efe6 0%,rgba(244,239,230,0) 75%),
      linear-gradient(180deg,#eee5dd 0%,#efd3dc 28%,#e8bcd8 55%,#dd9cca 80%,#cf8cbc 100%);
  }
  .brand{position:absolute;left:62px;top:82px;display:flex;align-items:center;gap:16px}
  .brand-dot{width:52px;height:52px;border-radius:50%;background:var(--cyan)}
  .brand-name{font-size:54px;color:#1e1e1e}

  .card{position:absolute;background:var(--card);border:2px solid;border-bottom-width:6px;border-radius:10px}
  .card.cyan{border-color:var(--cyan)}
  .card.green{border-color:var(--green)}
  .card.orange{border-color:var(--orange)}
  .card.pink{border-color:var(--pink)}
  .card.name-card{border-bottom-width:2px}

  .tab{position:absolute;color:#fff;font-size:18px;display:flex;align-items:center;justify-content:center;border-radius:8px}
  .tab.large{font-size:21px}
  .tab.cyan{background:var(--cyan)} .tab.green{background:var(--green)}
  .tab.orange{background:var(--orange)} .tab.pink{background:var(--pink)}

  .label{position:absolute;font-size:17px;line-height:1}
  .rule{position:absolute;height:1px;background:var(--ink)}
  .rules{position:absolute;background:repeating-linear-gradient(to bottom,transparent 0 27px,var(--ink) 27px 28px)}
  .boxes{position:absolute;display:flex;flex-direction:column;gap:8px}
  .box{width:20px;height:20px;border:1.5px solid #555;background:#fff}
  .check-list{position:absolute;list-style:none;font-size:18px}
  .check-list li{display:flex;align-items:center;gap:24px;height:30px}
  .check-list.tight li{gap:14px;height:26px}
  .check-list .box{width:18px;height:18px}
</style>
</head>
<body>
<div class="sheet">
  <div class="sheet-photo" role="img" aria-label="Soft-focus photograph of a smiling baby in a pink headband resting on pink blankets"></div>

  <div class="brand"><span class="brand-dot"></span><span class="brand-name">Velmora Notes</span></div>

  <section class="card cyan name-card" style="left:61px;top:207px;width:449px;height:97px"></section>
  <span class="label" style="left:87px;top:232px">NAME</span>
  <div class="rule" style="left:145px;top:248px;width:330px"></div>
  <span class="label" style="left:87px;top:272px">DATE</span>
  <div class="rule" style="left:145px;top:288px;width:330px"></div>

  <!-- Feeding -->
  <section class="card green" style="left:61px;top:342px;width:868px;height:185px"></section>
  <div class="tab green" style="left:383px;top:325px;width:223px;height:36px">FEEDING</div>
  <span class="label" style="left:87px;top:377px">Time</span>
  <span class="label" style="left:227px;top:377px">Milk (Type)</span>
  <span class="label" style="left:433px;top:377px">Water</span>
  <span class="label" style="left:625px;top:377px">Food</span>
  <span class="label" style="left:804px;top:377px">Amount</span>
  <div class="rules" style="left:87px;top:394px;width:50px;height:112px"></div>
  <div class="rules" style="left:195px;top:394px;width:145px;height:112px"></div>
  <div class="rules" style="left:384px;top:394px;width:144px;height:112px"></div>
  <div class="rules" style="left:572px;top:394px;width:145px;height:112px"></div>
  <div class="rules" style="left:761px;top:394px;width:144px;height:112px"></div>

  <!-- Nap time -->
  <section class="card cyan" style="left:61px;top:552px;width:278px;height:299px"></section>
  <div class="tab cyan" style="left:87px;top:535px;width:224px;height:37px">NAP TIME</div>
  <span class="label" style="left:87px;top:587px">Time</span>
  <span class="label" style="left:199px;top:587px">How Long</span>
  <div class="rules" style="left:87px;top:605px;width:50px;height:224px"></div>
  <div class="rules" style="left:166px;top:605px;width:140px;height:224px"></div>

  <!-- Diapers -->
  <section class="card orange" style="left:356px;top:552px;width:278px;height:299px"></section>
  <div class="tab orange" style="left:383px;top:537px;width:223px;height:37px">DIAPERS</div>
  <span class="label" style="left:382px;top:588px">Time</span>
  <span class="label" style="left:489px;top:588px">Wet</span>
  <span class="label" style="left:566px;top:588px">BM</span>
  <div class="rules" style="left:382px;top:607px;width:50px;height:224px"></div>
  <div class="boxes" style="left:495px;top:614px">
    <span class="box"></span><span class="box"></span><span class="box"></span><span class="box"></span>
    <span class="box"></span><span class="box"></span><span class="box"></span><span class="box"></span>
  </div>
  <div class="boxes" style="left:569px;top:614px">
    <span class="box"></span><span class="box"></span><span class="box"></span><span class="box"></span>
    <span class="box"></span><span class="box"></span><span class="box"></span><span class="box"></span>
  </div>

  <!-- Mood -->
  <section class="card pink" style="left:652px;top:552px;width:277px;height:299px"></section>
  <div class="tab pink" style="left:679px;top:537px;width:224px;height:37px">MOOD</div>
  <ul class="check-list" style="left:704px;top:606px">
    <li><span class="box"></span>Happy</li>
    <li><span class="box"></span>Sad</li>
    <li><span class="box"></span>Unsettled</li>
    <li><span class="box"></span>Energetic</li>
    <li><span class="box"></span>Tired</li>
    <li><span class="box"></span>Chatty</li>
    <li><span class="box"></span>Quiet</li>
  </ul>

  <!-- Today's activities -->
  <section class="card pink" style="left:61px;top:882px;width:868px;height:145px"></section>
  <div class="tab pink large" style="left:331px;top:862px;width:312px;height:38px">Today’s Activities</div>

  <!-- Supplies -->
  <section class="card orange" style="left:61px;top:1050px;width:868px;height:146px"></section>
  <div class="tab orange large" style="left:331px;top:1031px;width:312px;height:38px">Supplies Needed Soon</div>
  <ul class="check-list tight" style="left:129px;top:1093px">
    <li><span class="box"></span>Diapers</li>
    <li><span class="box"></span>Diaper Cream</li>
    <li><span class="box"></span>Other</li>
  </ul>
  <ul class="check-list tight" style="left:383px;top:1093px">
    <li><span class="box"></span>Milk/Formula</li>
    <li><span class="box"></span>Cereal</li>
  </ul>
  <ul class="check-list tight" style="left:690px;top:1093px">
    <li><span class="box"></span>Wet Wipes</li>
    <li><span class="box"></span>Baby Food</li>
  </ul>

  <!-- Special notes -->
  <section class="card green" style="left:61px;top:1219px;width:868px;height:146px"></section>
  <div class="tab green large" style="left:331px;top:1200px;width:312px;height:38px">Special Notes</div>
  <div class="rule" style="left:97px;top:1279px;width:776px"></div>
  <div class="rule" style="left:97px;top:1307px;width:776px"></div>
  <div class="rule" style="left:97px;top:1334px;width:776px"></div>
</div>
</body>
</html>
```